Online business manager needs a website

I need a website designed and then coded. I am an online business manager serving a number of different industries providing administrative support to existing small businesses and helping solo practitioners get their new business up and running.

I didn't have a logo formally designed but have been using the attached avatar and wouldn't mind something that incorporated that.

The business doesn't have an official name, so I've just been using my name Lena Pruvost, Online Business Manager or Lena Pruvost, OBM. I've attached two documents that I have made previously for an example of content.

I would prefer the final site be in Wordpress.

Requirements
Must have
• A way to contact me, testimonials, list of services

```html
<!DOCTYPE html>
<html lang="en">
<head>
<meta charset="utf-8">
<title>Lena Pruvost — Online Business Manager</title>
<link rel="stylesheet" href="https://fonts.googleapis.com/css2?family=Poppins:wght@300;400;500&family=Italianno&display=swap">
<style>
:root{
  --green:#167f5e;
  --green-soft:#8bc3ae;
  --green-bar:#3f9a77;
  --green-light:#2b8d6c;
  --placeholder:#e3ebe7;
  --grey-box:#f4f4f4;
  --text:#555;
  --ink:#222;
  --white:#fff;
  --line:#cfcfcf;
}
*{box-sizing:border-box;margin:0;padding:0}
html,body{width:1200px;height:4669px;overflow:hidden}
body{position:relative;background:var(--white);font-family:"Poppins",sans-serif;color:var(--text)}
.abs{position:absolute}
.script{font-family:"Italianno",cursive;font-weight:400}

/* header */
.site-header{left:0;top:0;width:1200px;height:131px;background:var(--white)}
.brand-mark{left:90px;top:40px;width:70px;height:70px;border:3px solid var(--green);border-radius:50%}
.brand-name{left:184px;top:38px;font-size:36px;font-weight:400;color:var(--green);letter-spacing:1px;line-height:1}
.brand-tag{left:184px;top:82px;font-size:14px;letter-spacing:2px;color:var(--text)}
.main-nav{left:569px;top:62px;display:flex;gap:25px;font-size:16px;color:var(--ink)}
.main-nav .current{color:var(--green)}

/* hero */
.hero{left:0;top:131px;width:1200px;height:581px;background:linear-gradient(100deg,#c9c2b6 0%,#e2ddd4 35%,#ebe8e3 60%,#dedbd6 100%)}
.hero-title{left:682px;top:215px;font-size:54px;font-weight:400;line-height:1.15;color:var(--ink)}
.hero-text{left:685px;top:358px;width:410px;font-size:14.5px;line-height:26px;color:#333}
.btn-outline{left:685px;top:470px;width:189px;height:65px;border:2px solid var(--green);border-radius:8px;color:var(--green);font-size:19px;display:flex;align-items:center;justify-content:center}

/* about */
.about-photo{border-radius:50%}
.about-photo.large{left:38px;top:908px;width:388px;height:388px;background:radial-gradient(circle at 50% 45%,#d9a98e 0%,#b88468 35%,#6d6a66 75%,#3e4a52 100%)}
.about-photo.small{left:303px;top:1148px;width:242px;height:242px;border:4px solid var(--white);background:radial-gradient(circle at 50% 45%,#e4b79f 0%,#c26f8f 45%,#8e2a5c 75%,#3d5a2e 100%)}
.about-box{left:600px;top:865px;width:515px;height:609px;background:var(--grey-box)}
.about-banner{left:633px;top:930px;width:451px;height:96px;background:var(--green)}
.avatar{background:var(--placeholder)}
.about-avatar{left:650px;top:872px;width:100px;height:154px}
.about-heading{left:758px;top:938px;font-size:60px;color:var(--white);line-height:1}
.about-text{left:641px;top:1064px;width:433px;font-size:14.5px;letter-spacing:.3px;line-height:30.8px;text-align:justify;text-align-last:center;color:var(--text)}

/* section headings */
.sec-avatar{width:130px;height:155px}
.sec-title{font-size:62px;color:var(--ink);line-height:1}
.sec-rule{height:2px;background:#777}

/* services */
.svc-card{background:var(--green-soft)}
.svc-card.side{top:1857px;height:600px;opacity:.95}
.svc-card.left{left:0;width:326px}
.svc-card.right{left:879px;width:321px;overflow:hidden}
.svc-img{left:0;top:0;width:100%;height:268px}
.svc-img.writing{background:linear-gradient(135deg,#b7d8cb,#a6cdbd 60%,#c4ddd3)}
.svc-img.desk{background:linear-gradient(135deg,#c7e0d6,#b3d5c8 60%,#9fc9b8)}
.svc-side-title{font-size:40px;color:var(--white);white-space:nowrap}
.svc-list{list-style:none;color:var(--white)}
.svc-list li{display:flex;align-items:center;gap:10px;white-space:nowrap}
.svc-list.small li{font-size:16px;height:31px}
.svc-list.big li{font-size:21px;height:31px}
.tick{width:16px;height:16px;flex:none}
.svc-center-frame{left:334px;top:1791px;width:540px;height:727px;border:1px solid #d6d6d6;background:var(--white)}
.svc-center{left:342px;top:1798px;width:523px;height:711px;background:var(--green)}
.svc-center-img{left:0;top:0;width:523px;height:298px;background:linear-gradient(160deg,#d8dfe3 0%,#aab4bb 40%,#5d6b75 70%,#2a3a48 100%)}
.svc-center-title{left:0;top:338px;width:523px;text-align:center;font-size:56px;line-height:62px;color:var(--white)}
.carousel-arrow{width:54px;height:54px;border-radius:50%;background:#222;display:flex;align-items:center;justify-content:center}

/* testimonial */
.quote-box{left:294px;top:3010px;width:785px;height:446px;background:var(--green);border-radius:36px}
.client-photo{left:150px;top:2888px;width:327px;height:312px;border:6px solid var(--white);border-radius:30px;background:linear-gradient(135deg,#8a9aa8 0%,#b07a5e 40%,#7a4a36 65%,#c9b3a0 100%)}
.quote-mark{left:538px;top:3041px;width:112px;height:112px;border-radius:50%;background:var(--white);display:flex;align-items:center;justify-content:center}
.quote-text{left:538px;top:3170px;width:452px;font-size:14.8px;line-height:31px;color:var(--white)}
.quote-name{left:538px;top:3342px;font-size:20px;font-weight:500;color:var(--white)}
.quote-company{left:538px;top:3370px;font-size:15px;color:var(--white)}
.btn-next{left:252px;top:3345px;width:102px;height:56px;background:var(--white);color:var(--green);font-size:15px;display:flex;align-items:center;justify-content:center;gap:8px}

/* contact */
.contact-photo{left:0;top:3671px;width:580px;height:523px;border-radius:0 262px 262px 0;background:linear-gradient(120deg,#d9d6d1 0%,#b59a86 30%,#3c4150 60%,#e8e6e2 100%)}
.field-label{left:645px;font-size:16px;color:var(--ink)}
.field{left:645px;width:468px;border-bottom:1px solid var(--line);font-size:14px;color:#888;padding-left:12px}
.btn-submit{left:645px;top:4110px;width:468px;height:56px;background:var(--green);border-radius:10px;color:var(--white);font-size:14px;display:flex;align-items:center;justify-content:center}

/* footer */
.site-footer{left:0;top:4279px;width:1200px;height:335px;background:var(--green)}
.footer-avatar{left:91px;top:4324px;width:235px;height:281px;background:var(--green-light)}
.footer-title{font-size:34px;color:var(--white);line-height:1}
.footer-links{left:373px;top:4400px;list-style:none;color:var(--white);font-size:15px}
.footer-links li{height:31px;display:flex;align-items:center;gap:10px}
.footer-links li::before{content:"";width:5px;height:5px;border-radius:50%;background:var(--white)}
.contact-list{left:562px;list-style:none;color:var(--white);font-size:15px}
.contact-item{display:flex;align-items:center;gap:12px;position:absolute;left:0;white-space:nowrap}
.icon-box{width:22px;height:22px;background:var(--white);border-radius:4px;display:flex;align-items:center;justify-content:center}
.news-text{left:863px;top:4410px;width:260px;font-size:15px;line-height:20px;color:var(--white)}
.news-input{left:863px;top:4465px;width:250px;height:37px;background:var(--white)}
.btn-subscribe{left:863px;top:4516px;width:125px;height:35px;background:#111;color:var(--white);font-size:13px;display:flex;align-items:center;justify-content:center}
.copyright{left:0;top:4614px;width:1200px;height:55px;background:var(--green-bar);color:var(--white);font-size:16px;display:flex;align-items:center;justify-content:center}
</style>
</head>
<body>

<header class="abs site-header">
  <div class="abs brand-mark"></div>
  <div class="abs brand-name">LENA PRUVOST</div>
  <div class="abs brand-tag">ONLINE BUSINESS MANAGER</div>
  <nav class="abs main-nav">
    <span class="current">Home</span><span>About Me</span><span>Services</span><span>Testimonials</span><span>Contact Me</span><span>Pricing</span>
  </nav>
</header>

<section class="abs hero" role="img" aria-label="Hands typing on a laptop on a white desk with glasses, pen and a plant"></section>
<h1 class="abs hero-title">Online Business<br>Manager</h1>
<p class="abs hero-text">Lorem ipsum dolor sit amet consectetur adipiscing elit. Etiam congue ex eros et semper diam suscipit non.Lorem ipsum dolor sit amet.</p>
<a class="abs btn-outline">CONTACT ME</a>

<div class="abs about-photo large" role="img" aria-label="Portrait photo of Lena smiling outdoors"></div>
<div class="abs about-photo small" role="img" aria-label="Portrait photo of Lena in front of flowering shrubs"></div>
<div class="abs about-box"></div>
<div class="abs about-banner"></div>
<div class="abs avatar about-avatar" role="img" aria-label="Cartoon avatar of Lena waving"></div>
<h2 class="abs about-heading script">About Me</h2>
<p class="abs about-text">Hi! I'm so excited that you have chosen to explore my portfolio. Helping businesses achieve their goals is my passion, and I'm thrilled that with my assistance you will have more time for your own passion project. I thrive while working independently, which means you can be confident when leaving tasks for me. The type of work that lights me up is anything involving organization and/or spreadsheets. You need data analyzed that includes multiple nested if formulas? You have an overwhelming amount of email to sort through and appointments to book? I'm your gal!</p>

<div class="abs avatar sec-avatar" style="left:341px;top:1545px" role="img" aria-label="Cartoon avatar of Lena waving"></div>
<div class="abs sec-rule" style="left:417px;top:1699px;width:319px"></div>
<h2 class="abs sec-title script" style="left:477px;top:1628px">My Services</h2>

<svg width="0" height="0" style="position:absolute">
  <symbol id="tick" viewBox="0 0 16 16"><rect x="1" y="2" width="12" height="12" fill="none" stroke="#fff" stroke-width="1.5"/><path d="M4 8l3 3 7-8" fill="none" stroke="#fff" stroke-width="2"/></symbol>
</svg>

<article class="abs svc-card side left">
  <div class="abs svc-img writing" role="img" aria-label="Typewriter page with a motivational writing quote"></div>
  <h3 class="abs svc-side-title script" style="left:36px;top:345px">Virtual Assistance</h3>
  <ul class="abs svc-list small" style="left:40px;top:420px">
    <li><svg class="tick"><use href="#tick"/></svg>Calendar Management</li>
    <li><svg class="tick"><use href="#tick"/></svg>Email Management</li>
    <li><svg class="tick"><use href="#tick"/></svg>Light Graphic Design</li>
    <li><svg class="tick"><use href="#tick"/></svg>Data Entry</li>
  </ul>
</article>

<article class="abs svc-card side right">
  <div class="abs svc-img desk" role="img" aria-label="Desk with calculator, keyboard and notebook"></div>
  <h3 class="abs svc-side-title script" style="left:55px;top:343px">Business Management</h3>
  <ul class="abs svc-list small" style="left:92px;top:408px">
    <li><svg class="tick"><use href="#tick"/></svg>Creation of Operating Procedures</li>
    <li><svg class="tick"><use href="#tick"/></svg>Review of Website Strategy</li>
    <li><svg class="tick"><use href="#tick"/></svg>Reporting and Analytics</li>
    <li><svg class="tick"><use href="#tick"/></svg>Project Management</li>
  </ul>
</article>

<div class="abs svc-center-frame"></div>
<article class="abs svc-center">
  <div class="abs svc-center-img" role="img" aria-label="Laptop on a desk beside printed calendars"></div>
  <h3 class="abs svc-center-title script">Social Media &amp;<br>Content Management</h3>
  <ul class="abs svc-list big" style="left:103px;top:482px">
    <li><svg class="tick"><use href="#tick"/></svg>Content Repurposing</li>
    <li><svg class="tick"><use href="#tick"/></svg>Graphics Creation</li>
    <li><svg class="tick"><use href="#tick"/></svg>Audiogram Creation</li>
    <li><svg class="tick"><use href="#tick"/></svg>Search Engine Optimization</li>
  </ul>
</article>

<div class="abs carousel-arrow" style="left:87px;top:2174px"><svg width="20" height="20" viewBox="0 0 20 20"><path d="M13 3L6 10l7 7" fill="none" stroke="#fff" stroke-width="2.5"/></svg></div>
<div class="abs carousel-arrow" style="left:1061px;top:2174px"><svg width="20" height="20" viewBox="0 0 20 20"><path d="M7 3l7 7-7 7" fill="none" stroke="#fff" stroke-width="2.5"/></svg></div>

<div class="abs avatar sec-avatar" style="left:384px;top:2674px" role="img" aria-label="Cartoon avatar of Lena waving"></div>
<div class="abs sec-rule" style="left:453px;top:2828px;width:263px"></div>
<h2 class="abs sec-title script" style="left:506px;top:2762px">Client Love</h2>

<div class="abs quote-box"></div>
<div class="abs client-photo" role="img" aria-label="Portrait photo of a smiling client"></div>
<div class="abs quote-mark"><svg width="56" height="40" viewBox="0 0 56 40"><circle cx="13" cy="14" r="10" fill="#167f5e"/><path d="M22 14c0 12-8 20-16 22" fill="none" stroke="#167f5e" stroke-width="5"/><circle cx="40" cy="14" r="10" fill="#167f5e"/><path d="M49 14c0 12-8 20-16 22" fill="none" stroke="#167f5e" stroke-width="5"/></svg></div>
<p class="abs quote-text">When it became apparent that a project would take more time than I had, Lena stepped up to take on the required research. She was thorough and timely; able to meet a last-minute 12-hour deadline. I would highly recommend Lena to assist with your next project.</p>
<div class="abs quote-name">Dana R. Owner,</div>
<div class="abs quote-company">Bright Ridge Roofing</div>
<a class="abs btn-next">Next <svg width="20" height="10" viewBox="0 0 20 10"><path d="M0 5h18M14 1l4 4-4 4" fill="none" stroke="#167f5e" stroke-width="1.5"/></svg></a>

<div class="abs contact-photo" role="img" aria-label="Hands typing on a laptop next to an open notebook and coffee cup"></div>
<div class="abs avatar sec-avatar" style="left:903px;top:3586px" role="img" aria-label="Cartoon avatar of Lena waving"></div>
<div class="abs sec-rule" style="left:638px;top:3738px;width:341px"></div>
<h2 class="abs sec-title script" style="left:647px;top:3670px">Contact Me</h2>

<form>
  <label class="abs field-label" style="top:3808px">Name</label>
  <div class="abs field" style="top:3842px;height:32px">Enter Your Name</div>
  <label class="abs field-label" style="top:3889px">Email</label>
  <div class="abs field" style="top:3922px;height:32px">Enter a valid emailaddress</div>
  <label class="abs field-label" style="top:3971px">Message</label>
  <div class="abs field" style="top:4000px;height:88px"></div>
  <a class="abs btn-submit">SUBMIT NOW</a>
</form>

<footer class="abs site-footer"></footer>
<div class="abs footer-avatar" role="img" aria-label="Cartoon avatar of Lena waving"></div>
<h4 class="abs footer-title script" style="left:373px;top:4343px">Quick Links</h4>
<ul class="abs footer-links">
  <li>About Me</li><li>Services</li><li>Testimonials</li><li>Contact Me</li><li>Pricing</li>
</ul>
<h4 class="abs footer-title script" style="left:562px;top:4343px">Contact Us</h4>
<ul class="abs contact-list" style="top:0">
  <li class="contact-item" style="top:4405px"><span class="icon-box"><svg width="14" height="14" viewBox="0 0 14 14"><path d="M3 1l2 3-1.5 1.5a8 8 0 0 0 5 5L10 9l3 2-1.5 2.5C6 13 1 8 .5 2.5z" fill="#167f5e"/></svg></span>555.014.2290</li>
  <li class="contact-item" style="top:4452px"><span class="icon-box"><svg width="14" height="12" viewBox="0 0 14 12"><rect x="1" y="1" width="12" height="10" fill="none" stroke="#167f5e" stroke-width="1.5"/><path d="M1 1l6 5 6-5" fill="none" stroke="#167f5e" stroke-width="1.5"/></svg></span>lena.pruvost.obm@example.com</li>
  <li class="contact-item" style="top:4491px"><span class="icon-box"></span>Lena Marie Pruvost</li>
  <li class="contact-item" style="top:4527px"><span class="icon-box"></span>/LenaPruvostOBM</li>
</ul>
<h4 class="abs footer-title script" style="left:863px;top:4343px">My Newsletter</h4>
<p class="abs news-text">Subscribe our newsletter to get the latest news.</p>
<div class="abs news-input"></div>
<a class="abs btn-subscribe">SUBSCRIBE</a>
<div class="abs copyright">Copyright © 2023 All Rights Reserved By Lena</div>

</body>
</html>
```